Bref créative
VELMORA BUSINESS CARDS
VELMORA BC
Professional
Anselmo Tribaldes
Director General
Fidencio Lozano 4817. Local 5 Altos.
Colonia Almendros.
Nuevo Laredo, Tamaulipas 88172.
Mexico.
anselmo@velmora-ejemplo.com
www.velmora-ejemplo.com
* Importacion y Exportacion.
* Comercializacion y Procura.
* Transporte LTL, Van Trailers, Flatbed, Oversize cargo.
* Soluciones de logistica.
* Aduanas.
Vector Logo file

```html
<!DOCTYPE html>
<html lang="es">
<head>
<meta charset="utf-8">
<title>VELMORA BC — Tarjetas de presentación</title>
<link href="https://fonts.googleapis.com/css2?family=Open+Sans:wght@400;600;700;800&display=swap" rel="stylesheet">
<style>
  :root {
    --bg: #e4e5e7;
    --card: #ffffff;
    --ink: #1b1b1f;
    --muted: #55585e;
    --blue-deep: #1c2a8c;
    --blue: #2b3fb8;
    --blue-light: #4a63d6;
    --gold: #f2c230;
    --grey-swoosh: #c9cbd0;
  }
  * { box-sizing: border-box; margin: 0; padding: 0; }
  html, body { width: 1200px; height: 799px; overflow: hidden; }
  body {
    background: var(--bg);
    font-family: "Open Sans", Arial, sans-serif;
    color: var(--ink);
    display: flex;
    align-items: center;
    justify-content: center;
    gap: 40px;
  }
  .card {
    position: relative;
    width: 540px;
    height: 309px;
    background: var(--card);
    overflow: hidden;
    box-shadow: 0 4px 14px rgba(0,0,0,0.12);
  }
  .brand {
    display: flex;
    align-items: center;
    gap: 10px;
  }
  .brand__name {
    font-weight: 800;
    letter-spacing: 1px;
    color: var(--ink);
  }
  .brand__dot {
    border-radius: 50%;
    background: var(--blue);
  }

  /* Back card */
  .card--back .services {
    position: absolute;
    top: 26px;
    right: 28px;
    width: 360px;
    text-align: right;
    font-size: 9.5px;
    line-height: 1.45;
    color: var(--muted);
    font-style: italic;
  }
  .card--back .brand {
    position: absolute;
    left: 50%;
    top: 52%;
    transform: translate(-50%, -50%);
  }
  .card--back .brand__name { font-size: 46px; }
  .card--back .brand__dot { width: 22px; height: 22px; }
  .card--back .website {
    position: absolute;
    left: 30px;
    bottom: 22px;
    font-size: 10px;
    font-weight: 600;
    color: var(--muted);
  }

  /* Front card */
  .card--front .shape { position: absolute; inset: 0; }
  .card--front .person {
    position: absolute;
    left: 28px;
    top: 40px;
    color: #fff;
  }
  .person__name { font-size: 18px; font-weight: 700; }
  .person__title { font-size: 10.5px; opacity: 0.85; margin-top: 1px; }
  .card--front .address {
    position: absolute;
    left: 28px;
    top: 128px;
    color: #fff;
    font-size: 10px;
    line-height: 1.4;
  }
  .card--front .contacts {
    position: absolute;
    left: 28px;
    top: 200px;
    list-style: none;
    color: #fff;
    font-size: 10px;
    line-height: 1.6;
  }
  .contacts li { display: flex; align-items: center; gap: 7px; }
  .contacts svg { width: 10px; height: 10px; flex: none; }
  .card--front .brand-block {
    position: absolute;
    right: 34px;
    top: 118px;
    display: flex;
    align-items: center;
    gap: 12px;
  }
  .card--front .brand__name { font-size: 30px; }
  .card--front .brand__dot { width: 14px; height: 14px; }
  .radio-id {
    font-size: 11px;
    font-weight: 700;
    color: var(--ink);
  }
</style>
</head>
<body>

  <section class="card card--back" aria-label="Reverso de la tarjeta">
    <p class="services">
      Flete Marítimo para Centro y Sudamérica &nbsp;•&nbsp; Flete Aéreo &nbsp;•&nbsp; Entregas Urgentes<br>
      Nuestra especialidad compras nacionales e internacionales con servicio de Puerta a Puerta
    </p>
    <div class="brand">
      <span class="brand__dot"></span>
      <span class="brand__name">VELMORA</span>
    </div>
    <p class="website">www.velmora-ejemplo.com</p>
  </section>

  <section class="card card--front" aria-label="Frente de la tarjeta">
    <svg class="shape" viewBox="0 0 540 309" preserveAspectRatio="none" aria-hidden="true">
      <defs>
        <linearGradient id="blueField" x1="0" y1="0" x2="1" y2="1">
          <stop offset="0" stop-color="var(--blue-light)"/>
          <stop offset="1" stop-color="var(--blue-deep)"/>
        </linearGradient>
      </defs>
      <path d="M0 0 H300 C250 60 235 120 250 185 C262 240 290 280 330 309 H0 Z" fill="url(#blueField)"/>
      <path d="M300 0 H330 C275 60 262 125 276 188 C288 242 316 282 358 309 H330 C290 280 262 240 250 185 C235 120 250 60 300 0 Z" fill="var(--blue)" opacity="0.55"/>
      <path d="M358 309 C316 282 288 242 276 188 C300 250 340 290 400 309 Z" fill="var(--grey-swoosh)"/>
    </svg>

    <div class="person">
      <p class="person__name">Anselmo Tribaldes</p>
      <p class="person__title">Director General</p>
    </div>

    <p class="address">
      Fidencio Lozano 4817. Local 5 Altos.<br>
      Colonia Almendros. Nuevo Laredo,<br>
      Tamaulipas 88172. Mexico.
    </p>

    <ul class="contacts">
      <li>
        <svg viewBox="0 0 10 10"><path d="M2 1 L4 1 L4.6 3 L3.4 3.8 C4 5.2 4.8 6 6.2 6.6 L7 5.4 L9 6 L9 8 C9 8.6 8.6 9 8 9 C4.2 9 1 5.8 1 2 C1 1.4 1.4 1 2 1 Z" fill="#fff"/></svg>
        867-555-0148
      </li>
      <li>
        <svg viewBox="0 0 10 10"><rect x="1.5" y="2.5" width="7" height="5" rx="0.6" fill="none" stroke="#fff" stroke-width="1"/><rect x="3" y="1" width="4" height="1.5" fill="#fff"/></svg>
        867-555-0192
      </li>
      <li>
        <svg viewBox="0 0 10 10"><rect x="1" y="2" width="8" height="6" fill="none" stroke="#fff" stroke-width="1"/><path d="M1 2 L5 5.5 L9 2" fill="none" stroke="#fff" stroke-width="1"/></svg>
        anselmo@velmora-ejemplo.com
      </li>
      <li>
        <svg viewBox="0 0 10 10"><circle cx="5" cy="5" r="4" fill="none" stroke="#fff" stroke-width="1"/><path d="M1 5 H9 M5 1 C3 3.5 3 6.5 5 9 M5 1 C7 3.5 7 6.5 5 9" fill="none" stroke="#fff" stroke-width="0.8"/></svg>
        www.velmora-ejemplo.com
      </li>
    </ul>

    <div class="brand-block">
      <div class="brand">
        <span class="brand__dot"></span>
        <span class="brand__name">VELMORA</span>
      </div>
      <span class="radio-id">52*904417*6</span>
    </div>
  </section>

</body>
</html>
```